Financial Planning business needs a new Business Card design

We need a business card design for an Australian financial planning business. I am looking for a clean simple design

Target Market(s)

People aged 25-40

Industry/Entity Type

Financial Service

Contact Information for Business Card

On the front of the card we need the following information:
Name: Derek Holloway (First Name Green: #006838 and last name Grey: #414042)
Position: Financial Adviser
Qualifications: BCom(Hons), AdvDipFP(WM), Dip FSMB, MWA
Mobile: 0437 215 604
Email: derek@mondlane.com.au

On the back of the card we need:
Postal address: PO BOX 5736, PERTH BC, WA 6849
Website: www.mondlane.com.au
Text: AFS Licence No. 518624

The fields need to be able to be edited.

Font styles to use
Sans Serif

Requirements
Must have
• Information listed above

```html
<!DOCTYPE html>
<html lang="en">
<head>
<meta charset="utf-8">
<title>Mondlane – Business Card</title>
<link rel="stylesheet" href="https://fonts.googleapis.com/css2?family=Arimo:wght@400;700&display=swap">
<style>
  :root {
    --page-bg: #3a332f;
    --card-bg: #141516;
    --card-edge: #1d1e20;
    --brand-green: #006838;
    --brand-grey: #414042;
    --text-light: #e6e6e6;
    --text-muted: #8a8b8d;
    --logo-silver: #6e6f72;
    --rule: #d9d9d9;
  }
  * { margin: 0; padding: 0; box-sizing: border-box; }
  html, body {
    width: 1200px;
    height: 864px;
    overflow: hidden;
    background: var(--page-bg);
    font-family: "Arimo", Arial, sans-serif;
  }
  .sheet {
    width: 1200px;
    height: 864px;
    display: flex;
    align-items: center;
    justify-content: center;
    gap: 40px;
  }
  .card {
    position: relative;
    width: 540px;
    height: 309px;
    background: var(--card-bg);
    border: 1px solid var(--card-edge);
    border-radius: 3px;
    box-shadow: 0 14px 30px rgba(0,0,0,0.45);
  }

  /* Back side */
  .card-back .wordmark {
    position: absolute;
    left: 50px;
    top: 92px;
    font-weight: 700;
    font-size: 44px;
    letter-spacing: 1px;
    color: var(--logo-silver);
  }
  .card-back .postal,
  .card-back .web-licence {
    position: absolute;
    left: 50px;
    font-size: 13px;
    letter-spacing: 0.3px;
    color: var(--text-muted);
  }
  .card-back .postal { top: 176px; }
  .card-back .web-licence { top: 200px; }

  /* Front side */
  .card-front .wordmark {
    position: absolute;
    right: 36px;
    top: 50px;
    font-weight: 700;
    font-size: 34px;
    letter-spacing: 1px;
    color: var(--brand-green);
  }
  .card-front .identity {
    position: absolute;
    left: 30px;
    top: 122px;
    right: 30px;
  }
  .name-line {
    font-size: 16px;
    color: var(--text-light);
  }
  .first-name { color: var(--brand-green); font-weight: 700; }
  .last-name { color: var(--brand-grey); font-weight: 700; }
  .qualifications {
    margin-top: 5px;
    font-size: 14px;
    color: var(--text-light);
    padding-bottom: 8px;
    border-bottom: 1px solid var(--rule);
  }
  .contact-list {
    list-style: none;
    margin-top: 12px;
  }
  .contact-item {
    display: flex;
    align-items: center;
    gap: 8px;
    font-size: 13px;
    color: var(--text-light);
    margin-bottom: 7px;
  }
  .contact-item svg { flex: none; }
</style>
</head>
<body>
<main class="sheet">

  <section class="card card-back" aria-label="Card back">
    <div class="wordmark">MONDLANE</div>
    <p class="postal">PO BOX 5736, KELLMORE BC, WA 6993</p>
    <p class="web-licence">www.mondlane.com.au &nbsp;|&nbsp; AFS Licence No. 518624</p>
  </section>

  <section class="card card-front" aria-label="Card front">
    <div class="wordmark">MONDLANE</div>
    <div class="identity">
      <p class="name-line">
        <span class="first-name">Derek</span> <span class="last-name">Holloway,</span> Financial Adviser
      </p>
      <p class="qualifications">BCom(Hons), AdvDipFP(WM), Dip FSMB, MWA</p>
      <ul class="contact-list">
        <li class="contact-item">
          <svg width="10" height="14" viewBox="0 0 10 14" aria-hidden="true">
            <rect x="1" y="0.8" width="8" height="12.4" rx="1.4" fill="none" stroke="var(--brand-green)" stroke-width="1.4"/>
            <rect x="4" y="10.6" width="2" height="1.2" fill="var(--brand-green)"/>
          </svg>
          <span>0437 215 604</span>
        </li>
        <li class="contact-item">
          <svg width="12" height="9" viewBox="0 0 12 9" aria-hidden="true">
            <rect x="0" y="0" width="12" height="9" rx="1" fill="var(--brand-green)"/>
            <path d="M0.6 0.8 L6 5 L11.4 0.8" fill="none" stroke="var(--card-bg)" stroke-width="1"/>
          </svg>
          <span>derek@mondlane.com.au</span>
        </li>
      </ul>
    </div>
  </section>

</main>
</body>
</html>
```